Local Flower Farm Needs Business Card Design

I need business cards designed for a flower farm based in Eudora, Kansas.
Business Info:
We are a local cut flower farm located in Eudora, Kansas, founded by Darla Hoffstrom. What started as a passion for agriculture and search for more joy in daily life has blossomed into a small business dedicated to providing the community with beautiful, fresh, and sustainable flowers. We specialize in local, seasonal blooms, ensuring that every petal reflects the care and dedication we pour into our craft. Our mission is to deliver the highest quality flowers directly to our customers through local farmers markets and to florists who share our commitment to sustainability. Join us in celebrating the beauty of nature, one bloom at a time!
Contact Details:
Darla Hoffstrom
Owner
Phone 913-555-0147
Facebook: Lorabelle Quinn Blossoms
Instagram: @LorabelleQuinnBlossoms
Website: LorabelleQuinnBlossoms.example
Target Market(s)
Wholesale to Florists and Direct to Consumer via Farmers Market
Industry/Entity Type
Florist, Farm
Contact Information for Business Card
Name, Contact Info, Logo
Look and feel

```html
<!DOCTYPE html>
<html lang="en">
<head>
<meta charset="utf-8">
<title>Lorabelle Quinn Blossoms – Business Cards</title>
<link rel="stylesheet" href="https://fonts.googleapis.com/css2?family=Cormorant+Garamond:wght@500;700&family=Lato:wght@400&display=swap">
<style>
  :root {
    --stage: #1c1c1c;
    --teal: #0b2a2e;
    --paper: #ffffff;
    --silver: #c8cdce;
    --ink-light: #f2f4f4;
    --ring: #0b2a2e;
  }
  * { box-sizing: border-box; margin: 0; padding: 0; }
  html, body { width: 1200px; height: 875px; overflow: hidden; }
  body {
    background: var(--stage);
    display: flex;
    align-items: center;
    justify-content: center;
    gap: 40px;
  }
  .card {
    position: relative;
    width: 540px;
    height: 309px;
    border-radius: 16px;
    background: var(--teal);
    overflow: hidden;
    box-shadow: 0 18px 40px rgba(0,0,0,.5);
  }
  .card-front { display: flex; align-items: center; justify-content: center; }

  .brand-seal {
    width: 190px; height: 190px;
    border-radius: 50%;
    display: flex; align-items: center; justify-content: center;
    text-align: center;
    font-family: "Cormorant Garamond", serif;
    font-weight: 700;
    font-size: 24px;
    line-height: 1.1;
    letter-spacing: .08em;
    text-transform: uppercase;
    padding: 20px;
  }
  .card-front .brand-seal { border: 1.5px solid var(--silver); color: var(--silver); }

  .seal-disc {
    position: absolute;
    left: 238px; top: -70px;
    width: 330px; height: 330px;
    border-radius: 50%;
    background: var(--paper);
    display: flex; align-items: center; justify-content: center;
  }
  .seal-disc .brand-seal {
    width: 170px; height: 170px;
    border: 1.5px solid var(--ring);
    color: var(--ring);
    font-size: 21px;
    margin-top: 60px;
    margin-left: -30px;
  }

  .contact-block {
    position: absolute;
    left: 38px; bottom: 34px;
    color: var(--ink-light);
    font-family: "Lato", sans-serif;
  }
  .person-name {
    font-family: "Cormorant Garamond", serif;
    font-weight: 700;
    font-size: 27px;
    line-height: .95;
    letter-spacing: .03em;
    text-transform: uppercase;
  }
  .person-role { font-size: 14px; margin-top: 2px; }
  .divider { width: 34px; height: 2px; background: var(--ink-light); margin: 14px 0 12px; }
  .contact-list { list-style: none; font-size: 13px; line-height: 1.6; }
  .contact-list li { display: flex; align-items: center; gap: 9px; }
  .contact-list svg { width: 11px; height: 11px; flex: none; }
</style>
</head>
<body>
  <section class="card card-front" aria-label="Card front">
    <div class="brand-seal">Lorabelle Quinn Blossoms</div>
  </section>

  <section class="card card-back" aria-label="Card back">
    <div class="seal-disc">
      <div class="brand-seal">Lorabelle Quinn Blossoms</div>
    </div>
    <div class="contact-block">
      <h1 class="person-name">Darla<br>Hoffstrom</h1>
      <p class="person-role">Owner</p>
      <div class="divider"></div>
      <ul class="contact-list">
        <li>
          <svg viewBox="0 0 24 24" aria-hidden="true"><path fill="#f2f4f4" d="M6.6 10.8a15 15 0 0 0 6.6 6.6l2.2-2.2a1 1 0 0 1 1-.25 11.4 11.4 0 0 0 3.6.57 1 1 0 0 1 1 1V20a1 1 0 0 1-1 1A17 17 0 0 1 3 4a1 1 0 0 1 1-1h3.5a1 1 0 0 1 1 1c0 1.25.2 2.45.57 3.57a1 1 0 0 1-.25 1z"/></svg>
          913-555-0147
        </li>
        <li>
          <svg viewBox="0 0 12 12" aria-hidden="true"><circle cx="6" cy="6" r="5" fill="#f2f4f4"/></svg>
          Lorabelle Quinn Blossoms
        </li>
        <li>
          <svg viewBox="0 0 12 12" aria-hidden="true"><circle cx="6" cy="6" r="5" fill="none" stroke="#f2f4f4" stroke-width="1.4"/></svg>
          @LorabelleQuinnBlossoms
        </li>
        <li>
          <svg viewBox="0 0 24 24" aria-hidden="true"><g fill="none" stroke="#f2f4f4" stroke-width="2"><circle cx="12" cy="12" r="10"/><path d="M2 12h20M12 2c3 3 3 17 0 20M12 2c-3 3-3 17 0 20"/></g></svg>
          LorabelleQuinnBlossoms.example
        </li>
      </ul>
    </div>
  </section>
</body>
</html>
```